Veltrium stationery design

Design stationery for us that fits with the colours of the logo. We are looking for letterheads, business cards etc. Something we can use for a prospectus and marketing presentations in power point. Must be completed in such a manner that it represents a corporate image for large enterprise clients and other large organisations. The company is a project assurance and monitoring company that works in all industries.

```html
<!DOCTYPE html>
<html lang="en">
<head>
<meta charset="utf-8">
<title>Veltrium business cards</title>
<link rel="stylesheet" href="https://fonts.googleapis.com/css2?family=Montserrat:wght@400;500;700;800&display=swap">
<style>
  :root {
    --navy: #02214a;
    --orange: #ff5a0a;
    --white: #ffffff;
    --rule: #8a9bb5;
    --backdrop: #3a3a3c;
  }
  * { margin: 0; padding: 0; box-sizing: border-box; }
  html, body {
    width: 1200px;
    height: 1200px;
    overflow: hidden;
    background: var(--backdrop);
    font-family: "Montserrat", Arial, sans-serif;
  }
  .sheet {
    position: relative;
    width: 1200px;
    height: 1200px;
  }
  .card {
    position: absolute;
    left: 150px;
    width: 900px;
    height: 514px;
    border-radius: 38px;
    overflow: hidden;
    border-bottom: 4px solid var(--orange);
    box-shadow: 0 14px 28px rgba(0,0,0,0.45);
  }
  .card--front { top: 56px; background: var(--white); }
  .card--back { top: 630px; background: var(--navy); }

  .wordmark {
    display: flex;
    align-items: center;
    gap: 22px;
    font-weight: 800;
    letter-spacing: 0.02em;
    text-transform: uppercase;
  }
  .wordmark__dot {
    border-radius: 50%;
    background: var(--orange);
    flex: none;
  }
  .card--front .wordmark {
    position: absolute;
    left: 0; right: 0; top: 78px;
    justify-content: center;
    font-size: 64px;
    color: var(--navy);
  }
  .card--front .wordmark__dot { width: 70px; height: 70px; }
  .card--back .wordmark {
    position: absolute;
    inset: 0;
    justify-content: center;
    font-size: 80px;
    color: var(--white);
  }
  .card--back .wordmark__dot { width: 88px; height: 88px; }

  .stripe {
    position: absolute;
    left: 0; right: 0;
    top: 250px;
    height: 10px;
    background: var(--orange);
  }
  .lower-band {
    position: absolute;
    left: 0; right: 0; bottom: 0;
    top: 272px;
    background: var(--navy);
  }
  .identity {
    position: absolute;
    left: 70px;
    bottom: 64px;
  }
  .identity__name {
    font-size: 46px;
    font-weight: 700;
    color: var(--orange);
    text-transform: uppercase;
    line-height: 1;
  }
  .identity__title {
    margin-top: 8px;
    font-size: 26px;
    font-weight: 500;
    color: var(--white);
    text-transform: uppercase;
  }
  .divider {
    position: absolute;
    left: 430px;
    top: 42px;
    width: 1px;
    height: 160px;
    background: var(--rule);
  }
  .contacts {
    position: absolute;
    left: 490px;
    top: 40px;
    list-style: none;
    display: flex;
    flex-direction: column;
    gap: 16px;
  }
  .contacts__item {
    display: flex;
    align-items: center;
    gap: 16px;
    font-size: 27px;
    color: var(--white);
  }
  .contacts__icon { width: 30px; height: 30px; flex: none; }
</style>
</head>
<body>
<main class="sheet">
  <section class="card card--front" aria-label="Business card front">
    <div class="wordmark"><span class="wordmark__dot"></span><span>Veltrium</span></div>
    <div class="stripe"></div>
    <div class="lower-band">
      <div class="identity">
        <p class="identity__name">Full Name</p>
        <p class="identity__title">Title</p>
      </div>
      <div class="divider"></div>
      <ul class="contacts">
        <li class="contacts__item">
          <svg class="contacts__icon" viewBox="0 0 24 24" aria-hidden="true"><path fill="#ff5a0a" d="M6.6 10.8a15.1 15.1 0 0 0 6.6 6.6l2.2-2.2c.3-.3.7-.4 1-.2 1.1.4 2.3.6 3.6.6.6 0 1 .4 1 1V20c0 .6-.4 1-1 1A17 17 0 0 1 3 4c0-.6.4-1 1-1h3.5c.6 0 1 .4 1 1 0 1.3.2 2.5.6 3.6.1.3 0 .7-.2 1z"/></svg>
          <span>(000) 000 0000</span>
        </li>
        <li class="contacts__item">
          <svg class="contacts__icon" viewBox="0 0 24 24" aria-hidden="true"><rect x="2" y="5" width="20" height="14" fill="#ff5a0a"/><path d="M2 5l10 8 10-8" fill="none" stroke="#02214a" stroke-width="1.6"/></svg>
          <span>email@company.com</span>
        </li>
        <li class="contacts__item">
          <svg class="contacts__icon" viewBox="0 0 24 24" aria-hidden="true"><g fill="none" stroke="#ff5a0a" stroke-width="1.8"><circle cx="12" cy="12" r="9.5"/><ellipse cx="12" cy="12" rx="4.2" ry="9.5"/><path d="M2.5 12h19M4 7h16M4 17h16"/></g></svg>
          <span>www.company.com</span>
        </li>
      </ul>
    </div>
  </section>

  <section class="card card--back" aria-label="Business card back">
    <div class="wordmark"><span class="wordmark__dot"></span><span>Veltrium</span></div>
  </section>
</main>
</body>
</html>
```